Building company business card

Design and print business cards for BRENTHOLM PTY LTD.
A residantial homes building company.
Mark Lantern already designed the company Logo.

```html
<!DOCTYPE html>
<html lang="en">
<head>
<meta charset="utf-8">
<title>BRENTHOLM PTY LTD – Business Card</title>
<link rel="stylesheet" href="https://fonts.googleapis.com/css2?family=Arimo:wght@400;700&family=Open+Sans:wght@400;700&display=swap">
<style>
  :root {
    --backdrop: #e9e5df;
    --card: #ffffff;
    --gold: #b8862b;
    --navy: #232a63;
    --ink: #2b2b2b;
  }
  * { margin: 0; padding: 0; box-sizing: border-box; }
  html, body { width: 900px; height: 1200px; overflow: hidden; }
  body { background: var(--backdrop); position: relative; font-family: "Open Sans", sans-serif; color: var(--ink); }

  .card {
    position: absolute;
    left: 78px;
    width: 744px;
    background: var(--card);
    border-radius: 36px;
    box-shadow: 0 3px 10px rgba(0,0,0,0.18);
    overflow: hidden;
  }
  .card--front { top: 130px; height: 443px; }
  .card--back { top: 638px; height: 440px; }

  .brand {
    position: absolute;
    display: flex;
    align-items: center;
    font-family: "Open Sans", sans-serif;
    font-weight: 700;
    color: var(--navy);
    letter-spacing: 0.5px;
  }
  .brand__square { background: var(--gold); flex: none; }
  .card--front .brand { left: 35px; top: 180px; font-size: 34px; gap: 10px; }
  .card--front .brand__square { width: 22px; height: 22px; }
  .card--back .brand { left: 0; right: 0; top: 250px; justify-content: center; font-size: 76px; gap: 20px; }
  .card--back .brand__square { width: 46px; height: 46px; }

  .holder { position: absolute; right: 35px; top: 188px; text-align: right; font-family: "Arimo", sans-serif; }
  .holder__name { font-size: 25px; font-weight: 700; color: var(--gold); line-height: 1; }
  .holder__role { font-size: 17px; color: var(--ink); margin-top: 12px; line-height: 1; }
  .tab { position: absolute; right: 0; top: 193px; width: 25px; height: 52px; background: var(--gold); }

  .rule { position: absolute; left: 35px; top: 252px; width: 669px; height: 2px; background: var(--gold); }

  .address { position: absolute; left: 35px; top: 267px; font-size: 18px; line-height: 30px; font-style: normal; }
  .contacts { position: absolute; left: 36px; top: 332px; list-style: none; font-size: 18px; }
  .contacts li { display: flex; align-items: center; height: 29.5px; }
  .contacts svg { width: 17px; height: 17px; margin-right: 10px; fill: var(--gold); flex: none; }
</style>
</head>
<body>
  <section class="card card--front" aria-label="Business card front">
    <div class="brand"><span class="brand__square"></span>BRENTHOLM</div>

    <div class="holder">
      <p class="holder__name">DORIAN (Dory) KESTREL</p>
      <p class="holder__role">Director</p>
    </div>
    <div class="tab"></div>
    <div class="rule"></div>

    <address class="address">PO Box 482<br>Kelverton East Vic 3190</address>

    <ul class="contacts">
      <li>
        <svg viewBox="0 0 20 20" aria-hidden="true"><path d="M2 7c0-3 4-4 8-4s8 1 8 4v1h-4V6.5c-1-.6-2.4-.8-4-.8s-3 .2-4 .8V8H2z"/><path d="M5 9h10l2 8H3z"/><circle cx="10" cy="13" r="2" fill="#fff"/></svg>
        0400 512 338
      </li>
      <li>
        <svg viewBox="0 0 20 20" aria-hidden="true"><path d="M6 1h8a1.5 1.5 0 0 1 1.5 1.5v15A1.5 1.5 0 0 1 14 19H6a1.5 1.5 0 0 1-1.5-1.5v-15A1.5 1.5 0 0 1 6 1zm0.5 2.5v11h7v-11zM10 15.5a1 1 0 1 0 0 2 1 1 0 0 0 0-2z"/></svg>
        0411 284 905
      </li>
      <li>
        <svg viewBox="0 0 20 20" aria-hidden="true"><path d="M3 5h14v1.2L10 11 3 6.2z"/><path d="M3 8l7 4.8L17 8v7H3z"/></svg>
        dk@brentholm-pl.co
      </li>
    </ul>
  </section>

  <section class="card card--back" aria-label="Business card back">
    <div class="brand"><span class="brand__square"></span>BRENTHOLM</div>
  </section>
</body>
</html>
```